"Velvet Petal Hour" Fashion Show Invitation design

We need an invitation design for our fashion show with the theme "Velvet Petal Hour"

the design will be the cover of the invitation, save the date cards, program etc

We are a philanthropic organization. Would like to incorporate florals, jewel tones or pastels etc... not sure if theres a way O or need) to incorporate fashion into that in an elegant way.

Text should read The Carrowfield Circle Presents "Velvet Petal Hour"
Updates

I'm looking for the design/image for the cover of our invitation- The only text needed is The Carrowfield Circle Presents Velvet Petal Hour I'm looking for feminine, elegant, florals etc...

Font styles to use
Serif
Decorative
Script

Colors
b768aa
e667a6
85cae6

Requirements
Must have
• jewel tones or pastels, flowers,
Nice to have
• fashion?

```html
<!DOCTYPE html>
<html lang="en">
<head>
<meta charset="utf-8">
<title>Velvet Petal Hour — Invitation</title>
<link rel="stylesheet" href="https://fonts.googleapis.com/css2?family=Bodoni+Moda:wght@400;500&family=Playfair+Display:wght@400&display=swap">
<style>
  :root {
    --backdrop: #ececec;
    --paper: #f4f1e7;
    --gold: #b3a77f;
    --orchid: #b768aa;
    --rose: #e667a6;
    --sky: #85cae6;
    --plum: #8a3f7c;
    --foliage-soft: rgba(214, 120, 182, 0.55);
    --foliage-cool: rgba(168, 150, 214, 0.5);
  }
  * { margin: 0; padding: 0; box-sizing: border-box; }
  html, body {
    width: 1200px; height: 1200px; overflow: hidden;
    background: var(--backdrop);
  }
  .invitation {
    position: absolute; left: 212px; top: 40px;
    width: 776px; height: 1120px;
    background: var(--paper);
    overflow: hidden;
    font-family: "Bodoni Moda", "Playfair Display", serif;
    text-align: center;
  }
  .foliage { position: absolute; }
  .foliage--top-left {
    left: -40px; top: -40px; width: 300px; height: 260px;
    background: radial-gradient(ellipse at 15% 15%, var(--foliage-soft), rgba(244,241,231,0) 68%);
  }
  .foliage--top-right {
    right: -40px; top: -40px; width: 300px; height: 260px;
    background: radial-gradient(ellipse at 85% 15%, var(--foliage-soft), rgba(244,241,231,0) 68%);
  }
  .foliage--left {
    left: 0; top: 220px; width: 120px; height: 520px;
    background: radial-gradient(ellipse at 0% 50%, var(--foliage-cool), rgba(244,241,231,0) 70%);
  }
  .foliage--right {
    right: 0; top: 220px; width: 120px; height: 520px;
    background: radial-gradient(ellipse at 100% 50%, var(--foliage-cool), rgba(244,241,231,0) 70%);
  }
  .foliage--bottom {
    left: 186px; bottom: 0; width: 404px; height: 80px;
    background: radial-gradient(ellipse at 50% 100%, rgba(183,104,170,0.7), rgba(244,241,231,0) 72%);
  }
  .sprig {
    position: absolute; top: 1000px; width: 60px; height: 56px;
    background: radial-gradient(ellipse, rgba(183,104,170,0.45), rgba(244,241,231,0) 70%);
  }
  .sprig--left { left: 146px; }
  .sprig--right { right: 146px; }

  .eyebrow {
    position: absolute; top: 108px; left: 0; width: 100%;
    font-size: 45px; font-weight: 400; letter-spacing: 2px;
    color: var(--gold);
  }
  .bloom-emblem {
    position: absolute; left: 154px; top: 185px;
    width: 470px; height: 470px; border-radius: 50%;
    background:
      radial-gradient(circle at 50% 50%, rgba(230,103,166,0.85) 0%, rgba(183,104,170,0.75) 45%, rgba(133,202,230,0.45) 75%, rgba(244,241,231,0) 100%);
  }
  .host {
    position: absolute; top: 745px; left: 0; width: 100%;
    font-size: 31px; letter-spacing: 1px;
    color: var(--rose);
    background: linear-gradient(90deg, var(--orchid), var(--rose) 50%, var(--orchid));
    -webkit-background-clip: text; background-clip: text;
    -webkit-text-fill-color: transparent;
  }
  .presents {
    position: absolute; top: 826px; left: 0; width: 100%;
    font-size: 14px; letter-spacing: 12px;
    color: var(--rose);
  }
  .show-title {
    position: absolute; top: 885px; left: 0; width: 100%;
    font-size: 52px; font-weight: 500; letter-spacing: 2px;
    background: linear-gradient(90deg, var(--sky) 0%, var(--orchid) 35%, var(--orchid) 65%, var(--rose) 100%);
    -webkit-background-clip: text; background-clip: text;
    -webkit-text-fill-color: transparent;
    color: var(--orchid);
  }
  .show-date {
    position: absolute; top: 963px; left: 0; width: 100%;
    font-family: "Playfair Display", "Bodoni Moda", serif;
    font-size: 31px; color: var(--plum);
  }
</style>
</head>
<body>
  <main class="invitation">
    <div class="foliage foliage--top-left" role="img" aria-label="Pastel pink leaf and sprig decoration"></div>
    <div class="foliage foliage--top-right" role="img" aria-label="Pastel pink leaf and sprig decoration"></div>
    <div class="foliage foliage--left" role="img" aria-label="Small lilac sprigs and leaves along the edge"></div>
    <div class="foliage foliage--right" role="img" aria-label="Small lilac sprigs and leaves along the edge"></div>

    <h2 class="eyebrow">INVITATION</h2>

    <div class="bloom-emblem" role="img" aria-label="Large stylised flower in pink, violet and sky blue"></div>

    <p class="host">THE CARROWFIELD CIRCLE</p>
    <p class="presents">present</p>
    <h1 class="show-title">VELVET PETAL HOUR</h1>
    <p class="show-date">Friday, May 24, 2019</p>

    <div class="sprig sprig--left" role="img" aria-label="Lilac leaf sprig"></div>
    <div class="sprig sprig--right" role="img" aria-label="Lilac leaf sprig"></div>
    <div class="foliage foliage--bottom" role="img" aria-label="Cluster of pink and violet leaves"></div>
  </main>
</body>
</html>
```